New legal process in family law needs graphic for home page of website

The new startup is called Harbourline Table in Australia. The idea is to offer a way of solving family law disputes by offering mediation and arbitration. That’s why it is an harbourline table – it is an alternative to the courts.
We need to encourage lawyers to refer clients to the service rather than going to court, so I would like a homepage graphic which is bright and interesting, and suggests to lawyers that this is a more sensible way of resolving family law disputes than spending a couple of years stuck in the court system.

Target Market(s)

Lawyers, family law clients

Industry/Entity Type

Family Law

Font styles to use
Serif
Sans Serif

Requirements
Nice to have
• My logo is uploaded below.

```html
<!DOCTYPE html>
<html lang="en">
<head>
<meta charset="utf-8">
<title>Harbourline Table – Home Page Banners</title>
<link rel="stylesheet" href="https://fonts.googleapis.com/css2?family=Hind:wght@400;500;600&display=swap">
<style>
  :root {
    --page-bg: #ffffff;
    --photo-light: #e9e4dc;
    --photo-sleeve: #8fa3b8;
    --photo-suit: #4f5d70;
    --photo-skin: #c98b6c;
    --photo-dark: #2d3440;
    --panel-blue: rgba(18, 160, 210, 0.86);
    --panel-frost: rgba(236, 236, 240, 0.84);
    --white: #ffffff;
    --navy: #3d4b95;
    --steel-blue: #6ba2c3;
  }
  * { box-sizing: border-box; margin: 0; padding: 0; }
  html, body {
    width: 1000px;
    height: 1200px;
    overflow: hidden;
    background: var(--page-bg);
    font-family: "Hind", Arial, sans-serif;
  }
  .banner {
    position: absolute;
    left: 120px;
    width: 778px;
    height: 320px;
    overflow: hidden;
  }
  .banner--intro { top: 63px; }
  .banner--cta { top: 430px; height: 319px; }
  .banner--light { top: 791px; }

  .banner__photo {
    position: absolute;
    inset: 0;
    background:
      radial-gradient(ellipse 120px 90px at 360px 230px, var(--photo-skin) 0%, transparent 70%),
      radial-gradient(ellipse 140px 80px at 200px 330px, var(--photo-skin) 0%, transparent 70%),
      radial-gradient(ellipse 260px 120px at 260px 150px, var(--photo-sleeve) 0%, transparent 75%),
      radial-gradient(ellipse 160px 120px at 60px 30px, var(--photo-light) 0%, transparent 80%),
      linear-gradient(120deg, #bfc6cc 0%, var(--photo-suit) 45%, var(--photo-dark) 70%, #b9ada0 100%);
  }
  .banner__panel {
    position: absolute;
    inset: 0;
    width: 778px;
    height: 320px;
  }
  .panel-shape--blue { fill: var(--panel-blue); }
  .panel-shape--frost { fill: var(--panel-frost); }

  .brand {
    position: absolute;
    left: 508px;
    top: 52px;
    width: 176px;
    color: var(--white);
  }
  .brand__row {
    display: flex;
    align-items: center;
    justify-content: space-between;
  }
  .brand__name {
    font-weight: 600;
    font-size: 19px;
    line-height: 20px;
    width: 132px;
    text-transform: uppercase;
    letter-spacing: 0.5px;
  }
  .brand__dot {
    width: 36px;
    height: 36px;
    border-radius: 50%;
    background: rgba(255, 255, 255, 0.55);
  }
  .brand__tagline {
    text-align: right;
    font-size: 10px;
    font-weight: 500;
    letter-spacing: 0.8px;
    margin-top: 1px;
  }
  .headline {
    position: absolute;
    left: 492px;
    top: 148px;
    width: 170px;
    text-align: center;
    color: var(--white);
    font-weight: 600;
    font-size: 15px;
    line-height: 19px;
  }
  .button {
    position: absolute;
    left: 521px;
    top: 215px;
    width: 113px;
    height: 28px;
    border: 2px solid var(--white);
    color: var(--white);
    font-weight: 600;
    font-size: 14px;
    line-height: 27px;
    text-align: center;
  }
  .banner--light .brand { color: var(--navy); }
  .banner--light .brand__dot { background: var(--steel-blue); }
  .banner--light .brand__tagline { color: var(--steel-blue); }
  .banner--light .headline { color: var(--steel-blue); }
  .banner--light .button { border-color: var(--navy); color: var(--navy); }
</style>
</head>
<body>

<section class="banner banner--intro">
  <div class="banner__photo" role="img" aria-label="Soft-focus photo of two professionals shaking hands across a meeting table"></div>
  <svg class="banner__panel" viewBox="0 0 778 320" aria-hidden="true">
    <polygon class="panel-shape--blue" points="497,0 743,0 660,320 414,320"/>
  </svg>
  <div class="brand">
    <div class="brand__row"><span class="brand__name">Harbourline Table</span><span class="brand__dot"></span></div>
    <div class="brand__tagline">Resolve Calmly</div>
  </div>
  <p class="headline">We solving family law disputes by mediation and arbitration</p>
</section>

<section class="banner banner--cta">
  <div class="banner__photo" role="img" aria-label="Soft-focus photo of two professionals shaking hands across a meeting table"></div>
  <svg class="banner__panel" viewBox="0 0 778 320" aria-hidden="true">
    <polygon class="panel-shape--blue" points="497,0 743,0 660,320 414,320"/>
  </svg>
  <div class="brand">
    <div class="brand__row"><span class="brand__name">Harbourline Table</span><span class="brand__dot"></span></div>
    <div class="brand__tagline">Resolve Calmly</div>
  </div>
  <p class="headline">We solving family law disputes by mediation and arbitration</p>
  <a class="button">Learn More</a>
</section>

<section class="banner banner--light">
  <div class="banner__photo" role="img" aria-label="Soft-focus photo of two professionals shaking hands across a meeting table"></div>
  <svg class="banner__panel" viewBox="0 0 778 320" aria-hidden="true">
    <polygon class="panel-shape--frost" points="497,0 743,0 660,320 414,320"/>
  </svg>
  <div class="brand">
    <div class="brand__row"><span class="brand__name">Harbourline Table</span><span class="brand__dot"></span></div>
    <div class="brand__tagline">Resolve Calmly</div>
  </div>
  <p class="headline">We solving family law disputes by mediation and arbitration</p>
  <a class="button">Learn More</a>
</section>

</body>
</html>
```